Need Business Cards for my Business

email address: rkpmarlowhollowworks@vendrimail.com
web address: rkpmarlowhollowworks.net
Slogan: We offer various QVN licenses
Rowland K. Pemberly
Please stick with colors of Company Logo
would like the card to be more of the color example of the logo.
If you need PDF copy of logo email me at the above account.
Creative control rests with you.

Industry/Entity Type

Business

Contact Information for Business Card

I am a minimalist, but would like something to pop and stand out amongst other cards, make it memorable.

Font styles to use
Serif
Decorative
Script

```html
<!DOCTYPE html>
<html lang="en">
<head>
<meta charset="utf-8">
<title>RKP Marlow Hollow Works — Business Card</title>
<link href="https://fonts.googleapis.com/css2?family=Arimo:wght@400;700&display=swap" rel="stylesheet">
<style>
  :root {
    --stage-dark: #333333;
    --stage-light: #5a5a5a;
    --paper: #ffffff;
    --brand-red: #e5232b;
    --brand-red-deep: #c01f2a;
    --brand-blue: #1a74b9;
    --brand-navy: #15365f;
    --ink-navy: #1b4f8a;
    --text-light: #ffffff;
  }
  * { box-sizing: border-box; margin: 0; padding: 0; }
  html, body { width: 999px; height: 1200px; overflow: hidden; }
  body {
    position: relative;
    font-family: "Arimo", Helvetica, Arial, sans-serif;
    background: radial-gradient(ellipse at center, var(--stage-light) 0%, var(--stage-dark) 100%);
  }
  .card {
    position: absolute;
    left: 22px;
    width: 943px;
    height: 540px;
    overflow: hidden;
    box-shadow: 0 0 6px rgba(0,0,0,.35);
  }

  /* Shared brand block */
  .brand {
    display: flex; flex-direction: column; align-items: center; justify-content: center;
  }
  .brand__row { display: flex; align-items: center; gap: 22px; }
  .brand__mark { width: 46px; height: 46px; background: var(--brand-red); flex: none; }
  .brand__name { font-weight: 700; font-size: 46px; color: var(--ink-navy); letter-spacing: .5px; line-height: 1; }
  .brand__slogan {
    margin-top: 14px; padding-left: 68px;
    font-weight: 700; font-size: 20px; letter-spacing: 1.5px; color: var(--ink-navy);
    text-transform: uppercase;
  }

  /* Front */
  .card--front { top: 56px; background: var(--paper); }
  .front__brand { position: absolute; left: 0; top: 0; width: 100%; height: 277px; }
  .front__rule { position: absolute; left: 0; top: 277px; width: 100%; height: 9px; background: var(--brand-red); }
  .front__panel {
    position: absolute; left: 0; top: 286px; width: 100%; height: 254px;
    background: linear-gradient(180deg, var(--brand-blue) 0%, var(--brand-navy) 100%);
  }
  .holder-name {
    position: absolute; left: 37px; top: 182px;
    color: var(--text-light); font-weight: 700; font-size: 31px; line-height: 1;
  }
  .contact-list { position: absolute; left: 485px; top: 30px; list-style: none; }
  .contact-list li {
    display: flex; align-items: center; gap: 12px; height: 44px; margin-bottom: 8.5px;
    color: var(--text-light); font-size: 21px; white-space: nowrap;
  }
  .contact-icon {
    width: 44px; height: 40px; background: var(--brand-red); flex: none;
    display: flex; align-items: center; justify-content: center;
  }
  .contact-icon svg { width: 22px; height: 22px; }

  /* Back */
  .card--back {
    top: 617px;
    background: linear-gradient(90deg, var(--brand-blue) 0%, var(--brand-navy) 100%);
  }
  .back__brand { position: absolute; left: 0; top: 0; width: 100%; height: 440px; }
  .back__brand .brand__row { gap: 24px; }
  .back__brand .brand__mark { background: var(--text-light); width: 50px; height: 50px; }
  .back__brand .brand__name { color: var(--text-light); font-size: 50px; }
  .back__brand .brand__slogan { color: var(--text-light); font-size: 22px; padding-left: 74px; }
  .back__band {
    position: absolute; left: 0; top: 440px; width: 100%; height: 44px;
    background: linear-gradient(90deg, var(--brand-red) 0%, var(--brand-red-deep) 100%);
    display: flex; align-items: center; justify-content: center;
    color: var(--text-light); font-size: 24px; letter-spacing: 4.5px;
    padding-right: 30px;
  }
</style>
</head>
<body>

<section class="card card--front">
  <div class="brand front__brand">
    <div class="brand__row">
      <span class="brand__mark"></span>
      <span class="brand__name">RKP Marlow Hollow Works</span>
    </div>
    <p class="brand__slogan">We offer various QVN licenses</p>
  </div>
  <div class="front__rule"></div>
  <div class="front__panel">
    <p class="holder-name">Rowland K. Pemberly</p>
    <ul class="contact-list">
      <li>
        <span class="contact-icon"><svg viewBox="0 0 24 24" fill="#fff"><path d="M6.6 10.8c1.4 2.8 3.8 5.1 6.6 6.6l2.2-2.2c.3-.3.7-.4 1-.2 1.1.4 2.3.6 3.6.6.6 0 1 .4 1 1V20c0 .6-.4 1-1 1C10.6 21 3 13.4 3 4c0-.6.4-1 1-1h3.5c.6 0 1 .4 1 1 0 1.3.2 2.5.6 3.6.1.3 0 .7-.2 1z"/></svg></span>
        00 0000 0000
      </li>
      <li>
        <span class="contact-icon"><svg viewBox="0 0 24 24" fill="none" stroke="#fff" stroke-width="2"><rect x="7" y="3" width="10" height="18" rx="1.5"/><line x1="10" y1="18" x2="14" y2="18"/></svg></span>
        0000 000 000
      </li>
      <li>
        <span class="contact-icon"><svg viewBox="0 0 24 24" fill="#fff"><path d="M3 9l9-6 9 6v11H3z"/><path d="M3 9l9 6 9-6" fill="none" stroke="#e5232b" stroke-width="1.6"/></svg></span>
        rkpmarlowhollowworks@vendrimail.com
      </li>
      <li>
        <span class="contact-icon"><svg viewBox="0 0 24 24" fill="none" stroke="#fff" stroke-width="1.6"><circle cx="12" cy="12" r="9"/><ellipse cx="12" cy="12" rx="4" ry="9"/><line x1="3" y1="12" x2="21" y2="12"/><line x1="4.5" y1="7.5" x2="19.5" y2="7.5"/><line x1="4.5" y1="16.5" x2="19.5" y2="16.5"/></svg></span>
        rkpmarlowhollowworks.net
      </li>
    </ul>
  </div>
</section>

<section class="card card--back">
  <div class="brand back__brand">
    <div class="brand__row">
      <span class="brand__mark"></span>
      <span class="brand__name">RKP Marlow Hollow Works</span>
    </div>
    <p class="brand__slogan">We offer various QVN licenses</p>
  </div>
  <div class="back__band">rkpmarlowhollowworks.net</div>
</section>

</body>
</html>
```